Home page graphic design only (NOT WEBSITE DESIGN)

I require a home page to be designed for my new website.
I DO NOT REQUIRE to build a website. We are a rug company specialising in alpaca wool. It is targeted at the high end of the market and hence the graphics of our page requires to reflect this. Our current page is as per attachment and I think it is too basic.
Updates

Target Market(s)

Extremly high net worth individuals where luxury is a requirement

Requirements
Must have
• show of style, luxury, uniqueness. Prefer having bright images.
Nice to have
• a highly sofisticated roomscape where the focus in the rug. See attachment as an example
Should not have
• Not sure

```html
<!DOCTYPE html>
<html lang="en">
<head>
<meta charset="utf-8">
<title>Maison Lanière — Exquisite Luxury</title>
<link rel="stylesheet" href="https://fonts.googleapis.com/css2?family=Cormorant+Garamond:wght@500&family=Playfair+Display:wght@700&family=Work+Sans:wght@400;600&family=Allura&display=swap">
<style>
  :root {
    --page: #ffffff;
    --gold: #f2b92c;
    --tan: #d8bd80;
    --white: #ffffff;
    --slate: #616161;
    --ink: #000000;
    --sage-veil: rgba(214, 213, 163, 0.86);
    --rule: rgba(255, 255, 255, 0.55);
  }
  * { margin: 0; padding: 0; box-sizing: border-box; }
  html, body {
    width: 1200px; height: 2188px; overflow: hidden;
    background: var(--page);
  }
  .canvas { position: relative; width: 1200px; height: 2188px; }

  .banner {
    position: absolute; left: 47px; width: 1105px; height: 683px; overflow: hidden;
  }
  .banner--sage { top: 42px; }
  .banner--slate { top: 751px; background: var(--slate); }
  .banner--noir { top: 1460px; background: var(--ink); }

  .photo {
    position: absolute;
    background: linear-gradient(180deg, #e4e4da 0%, #cfcbb6 38%, #c8bf9f 62%, #bdb392 82%, #5e5d58 100%);
  }
  .banner--sage .photo { inset: 0; }
  .banner--slate .photo,
  .banner--noir .photo { left: 492px; top: 55px; width: 558px; height: 575px;
    background: linear-gradient(180deg, #8d9486 0%, #b9ae92 25%, #d2c5a6 45%, #c6bd9e 72%, #6a6964 100%); }

  .veil {
    position: absolute; left: 556px; top: 0; width: 549px; height: 683px;
    background: var(--sage-veil);
  }

  .copy { position: absolute; top: 0; width: 0; height: 683px; }
  .banner--sage .copy { left: 831px; }
  .banner--slate .copy, .banner--noir .copy { left: 258px; }

  .line {
    position: absolute; left: 0; transform: translateX(-50%);
    white-space: nowrap; line-height: 1; text-align: center;
  }
  .brand-name {
    font-family: "Cormorant Garamond", serif; font-weight: 500;
    font-size: 42px; color: var(--gold);
  }
  .headline {
    font-family: "Playfair Display", serif; font-weight: 700;
    font-size: 45px; letter-spacing: 1px;
  }
  .subline {
    font-family: "Playfair Display", serif; font-weight: 400;
    font-size: 17px; letter-spacing: 2px;
  }
  .signature {
    font-family: "Allura", cursive; font-size: 40px;
  }
  .meta {
    font-family: "Work Sans", sans-serif; font-weight: 400;
    font-size: 17px; letter-spacing: 1.5px;
  }
  .regions {
    display: flex; align-items: center;
    font-family: "Work Sans", sans-serif; font-weight: 600;
    font-size: 15px; letter-spacing: 1.2px; color: var(--white);
  }
  .regions li { list-style: none; padding: 0 17px; border-left: 1px solid var(--rule); line-height: 24px; }
  .regions li:first-child { border-left: none; }

  .banner--sage .headline,
  .banner--sage .subline,
  .banner--sage .signature,
  .banner--sage .meta { color: var(--white); }
  .banner--slate .headline, .banner--noir .headline,
  .banner--slate .subline, .banner--noir .subline,
  .banner--slate .signature, .banner--noir .signature,
  .banner--slate .meta, .banner--noir .meta { color: var(--tan); }

  .banner--sage .brand-name { top: 221px; }
  .banner--sage .headline { top: 272px; }
  .banner--sage .subline { top: 343px; }
  .banner--sage .signature { top: 375px; }
  .banner--sage .established { top: 505px; }
  .banner--sage .regions { top: 540px; }
  .banner--sage .company { top: 586px; }
  .banner--sage .abn { top: 625px; }

  .banner--slate .brand-name, .banner--noir .brand-name { top: 196px; }
  .banner--slate .headline, .banner--noir .headline { top: 249px; }
  .banner--slate .subline, .banner--noir .subline { top: 319px; }
  .banner--slate .signature, .banner--noir .signature { top: 353px; }
  .banner--slate .established, .banner--noir .established { top: 484px; left: -10px; }
  .banner--slate .regions, .banner--noir .regions { top: 519px; }
  .banner--slate .company, .banner--noir .company { top: 562px; left: 45px; }
  .banner--slate .abn, .banner--noir .abn { top: 600px; left: 45px; }
</style>
</head>
<body>
<main class="canvas">

  <section class="banner banner--sage">
    <div class="photo" role="img" aria-label="Bright penthouse living room with a beige sofa, white coffee table and a textured alpaca rug, city view through tall windows"></div>
    <div class="veil"></div>
    <div class="copy">
      <p class="line brand-name">Maison Lanière</p>
      <h1 class="line headline">EXQUISITE LUXURY</h1>
      <p class="line subline">CARPETING AND AREA RUGS MADE</p>
      <p class="line signature">from pure peruvian alphaca</p>
      <p class="line meta established">Established in 1988</p>
      <ul class="line regions"><li>AUSTRALIA</li><li>USA</li><li>EUROPE</li><li>UK</li><li>ASIA</li><li>UAE</li></ul>
      <p class="line meta company">Maison Lanière Pty Ltd</p>
      <p class="line meta abn">ABN 12 345 678 901</p>
    </div>
  </section>

  <section class="banner banner--slate">
    <div class="photo" role="img" aria-label="Close view of a beige sofa resting on a textured alpaca area rug by tall city windows"></div>
    <div class="copy">
      <p class="line brand-name">Maison Lanière</p>
      <h1 class="line headline">EXQUISITE LUXURY</h1>
      <p class="line subline">CARPETING AND AREA RUGS MADE</p>
      <p class="line signature">from pure peruvian alphaca</p>
      <p class="line meta established">Established in 1988</p>
      <ul class="line regions"><li>AUSTRALIA</li><li>USA</li><li>EUROPE</li><li>UK</li><li>ASIA</li><li>UAE</li></ul>
      <p class="line meta company">Maison Lanière Pty Ltd</p>
      <p class="line meta abn">ABN 12 345 678 901</p>
    </div>
  </section>

  <section class="banner banner--noir">
    <div class="photo" role="img" aria-label="Close view of a beige sofa resting on a textured alpaca area rug by tall city windows"></div>
    <div class="copy">
      <p class="line brand-name">Maison Lanière</p>
      <h1 class="line headline">EXQUISITE LUXURY</h1>
      <p class="line subline">CARPETING AND AREA RUGS MADE</p>
      <p class="line signature">from pure peruvian alphaca</p>
      <p class="line meta established">Established in 1988</p>
      <ul class="line regions"><li>AUSTRALIA</li><li>USA</li><li>EUROPE</li><li>UK</li><li>ASIA</li><li>UAE</li></ul>
      <p class="line meta company">Maison Lanière Pty Ltd</p>
      <p class="line meta abn">ABN 12 345 678 901</p>
    </div>
  </section>

</main>
</body>
</html>
```